Mediapreneur looking for Wordpress Design for 55 plus community

I own the domain brightyearsnook.com and I have another contest going on to design the logo. I'm looking to build a site for those 55 plus who are living an active lifestyle.
I want to base my site off of this site, except make it more friendly to the 55 and over community.
http://www.tallowcrest.com/
In my menu, I'd like to have the following categories. About Listen Read Watch Forum Contact and the ability to add more categories in the future (possible to external sites).
Listen will be podcasts, read will be blog posts, and watch will be videos (webinars)
Updates
I uploaded some images I bought from Pixelgrove that could be used in the design. Possibly a collage.
Videos are actually going to be webinars in the future. For example, I see a real estate agent presenting a webinar about active communities, or a financial adviser giving financial advice to my community. I was trying to simplify it for my audience, some of whom may not know what a webinar is, but I'd like to go with Webinar instead of Watch. I like read and listen, though. I plan on monetizing the site via sponsorship in podcasts and a directory of active communities I'm building. I'm possibly going to ask for sponsorship for webinars and write e-books in the future. Could you display podcasts on the home page? Maybe put the most recent blog posts below the podcasts? Also, can you put a form asking them to join my newsletter somewhere in prominent position? My call to actions are to get them to subscribe to my mailing list and listen to podcasts.
Thanks.
I changed my mind on using Webinar in the menu. I asked my mom what a webinar was and she gave me a blank look. I like the idea of using Watch instead. The menu should be in this order About Listen Read Watch Forum. Please put contact details in the header menu above the menu. Call...make up a phone number. Email..contact@brightyearsnook.com. In case you missed one of my previous public updates, Listen = Podcast, Read = Blog, and Watch = Webinar/Video.
Thanks and sorry for the changes.
55 and over
Build

```html
<!DOCTYPE html>
<html lang="en">
<head>
<meta charset="utf-8">
<title>Bright Years Nook — Home</title>
<link rel="stylesheet" href="https://fonts.googleapis.com/css2?family=Roboto:wght@400;500;700;900&family=Lato:wght@400;700&display=swap">
<style>
:root{
  --green-deep:#0e6a36;
  --lime:#8dc63f;
  --lime-soft:rgba(141,198,63,.78);
  --charcoal:#383838;
  --footer:#2d2d2d;
  --paper:#e9e9e9;
  --card:#f7f7f7;
  --ink:#333;
  --white:#fff;
}
*{box-sizing:border-box;margin:0;padding:0}
html,body{width:672px;height:1200px;overflow:hidden}
body{position:relative;font-family:"Lato",sans-serif;color:var(--ink);background:var(--paper)}
.abs{position:absolute}

/* hero */
.hero{left:0;top:0;width:672px;height:363px;background:
  radial-gradient(ellipse 90px 120px at 40px 190px,#2f3550 0%,transparent 100%),
  radial-gradient(ellipse 110px 140px at 290px 260px,#e0a92a 0%,transparent 100%),
  radial-gradient(ellipse 120px 140px at 530px 250px,#4a76b8 0%,transparent 100%),
  linear-gradient(100deg,#6d7a86 0%,#d9b66a 30%,#c9a07a 55%,#6f8fb8 78%,#8c7a60 100%)}
.hero-caption{left:136px;top:181px;width:376px;height:41px;background:var(--lime-soft);color:var(--white);font-family:"Roboto",sans-serif;font-weight:700;font-size:16px;letter-spacing:.6px;display:flex;align-items:center;justify-content:center}
.hero-arrow{top:190px;width:18px;height:32px}
.hero-arrow.prev{left:24px}
.hero-arrow.next{left:630px}

/* header */
.site-header{left:0;top:0;width:672px;height:56px;background:rgba(20,24,20,.62)}
.brand{left:76px;top:14px;display:flex;align-items:center;gap:5px;font-family:"Roboto",sans-serif;font-weight:700;font-size:12px;line-height:14px;color:var(--lime)}
.brand-dot{width:8px;height:8px;border-radius:50%;background:var(--lime);flex:none}
.main-nav{left:262px;top:20px;display:flex}
.nav-item{width:50px;display:flex;flex-direction:column;align-items:center;font-family:"Roboto",sans-serif;font-weight:500;font-size:10px;color:var(--lime)}
.nav-item svg{width:16px;height:16px;margin-bottom:3px;fill:none;stroke:var(--lime);stroke-width:1.4}
.nav-item.is-current{color:var(--white)}
.nav-item.is-current svg{stroke:var(--white)}

/* welcome */
.welcome{left:0;top:363px;width:672px;height:127px;background:var(--green-deep);color:var(--white);text-align:center}
.welcome h1{margin-top:18px;font-family:"Roboto",sans-serif;font-weight:700;font-size:19px;letter-spacing:.3px}
.welcome .rule{width:124px;height:1px;background:rgba(255,255,255,.5);margin:4px auto 7px}
.welcome p{width:548px;margin:0 auto;font-size:8.4px;line-height:13.8px}

/* features */
.features{left:0;top:490px;width:672px;height:192px;background:var(--charcoal)}
.feature{top:26px;width:137px;text-align:center}
.feature .thumb{width:137px;height:90px;border:2px solid var(--white)}
.feature h2{margin-top:6px;font-family:"Roboto",sans-serif;font-weight:500;font-size:11.5px;color:var(--lime)}
.feature p{margin-top:2px;font-size:7.6px;line-height:11px;color:#eee}
.feature .more{display:block;margin-top:4px;font-size:8px;color:var(--lime)}

/* content */
.content{left:0;top:682px;width:672px;height:494px;background:var(--paper)}
.post{left:56px;width:359px;height:115px;background:var(--card);box-shadow:0 1px 3px rgba(0,0,0,.12)}
.post .thumb{left:0;top:0;width:115px;height:115px}
.post h3{left:130px;top:17px;font-family:"Lato",sans-serif;font-weight:400;font-size:11.5px;color:#333}
.post .meta{left:130px;top:36px;display:flex;gap:11px;font-size:6.2px;color:#555;align-items:center}
.post .meta span{display:flex;align-items:center;gap:3px}
.post .meta svg{width:7px;height:7px;fill:var(--lime)}
.post p{left:130px;top:53px;width:216px;font-size:6.6px;line-height:10.4px;color:#333}
.post .go{left:341px;top:96px;width:19px;height:19px;background:var(--lime);display:flex;align-items:center;justify-content:center}
.spinner{left:222px;top:1116px;width:24px;height:24px}

/* sidebar */
.promo{box-shadow:0 1px 3px rgba(0,0,0,.2)}
.promo-photo{left:432px;top:700px;width:184px;height:130px;background:linear-gradient(160deg,#7fb4d8 0%,#bcd7e6 45%,#d8c9a6 75%,#6f8094 100%)}
.promo-photo .headline{position:absolute;right:6px;top:10px;text-align:right;font-family:"Roboto",sans-serif;font-size:11px;line-height:13px;color:var(--white)}
.promo-photo .headline small{display:block;font-size:8px}
.promo-photo .cta{position:absolute;left:94px;top:70px;width:84px;height:17px;background:var(--lime);font-family:"Roboto",sans-serif;font-weight:700;font-size:6.6px;color:#16331a;text-align:center;line-height:17px}
.promo-photo .badge{position:absolute;top:95px;width:40px;height:14px;background:#111;border-radius:2px}
.promo-retire{left:432px;top:838px;width:91px;height:141px;background:linear-gradient(180deg,#6c8f3f 0%,#a9b8a0 55%,#e6e2d6 100%)}
.promo-retire .caption{position:absolute;left:0;bottom:0;width:91px;padding:3px 4px;background:rgba(255,255,255,.85);font-family:"Roboto",sans-serif;font-weight:700;font-size:10px;line-height:11.5px;color:#222}
.promo-travel{left:526px;top:838px;width:90px;height:141px;background:linear-gradient(180deg,#0d79b8 0%,#1fa3c7 60%,#3f8a5a 100%)}
.promo-travel .label{position:absolute;right:4px;top:10px;width:80px;text-align:right;font-size:5.4px;line-height:7px;color:var(--white)}
.promo-travel .tag{position:absolute;right:4px;bottom:12px;width:24px;height:12px;background:#d21f26}
.promo-books{left:432px;top:990px;width:184px;height:154px;background:linear-gradient(150deg,#3a1a10 0%,#6e2e1a 45%,#a0582a 75%,#2a120a 100%)}
.promo-books .line{position:absolute;left:3px;top:44px;font-family:"Roboto",sans-serif;font-weight:900;font-size:6.6px;color:var(--white)}

/* footer */
.site-footer{left:0;top:1176px;width:672px;height:24px;background:var(--footer);color:#ddd;font-size:8.6px;text-align:center;line-height:24px}
</style>
</head>
<body>

<div class="abs hero" role="img" aria-label="Photo of four smiling older friends playing dominoes at a table"></div>
<div class="abs hero-caption">HELPING YOU LIVE AN ACTIVE LIFESTYLE</div>
<svg class="abs hero-arrow prev" viewBox="0 0 18 32"><path d="M16 2 2 16l14 14" fill="none" stroke="#fff" stroke-width="2"/></svg>
<svg class="abs hero-arrow next" viewBox="0 0 18 32"><path d="M2 2l14 14L2 30" fill="none" stroke="#fff" stroke-width="2"/></svg>

<header class="abs site-header">
  <div class="abs brand"><span class="brand-dot"></span><span>Bright Years<br>Nook</span></div>
  <nav class="abs main-nav">
    <a class="nav-item is-current"><svg viewBox="0 0 16 16"><path d="M2 8 8 2l6 6M4 7v7h8V7"/></svg>Home</a>
    <a class="nav-item"><svg viewBox="0 0 16 16"><circle cx="8" cy="8" r="7"/><circle cx="8" cy="6.5" r="2.3"/><path d="M4 13c1-2.5 7-2.5 8 0"/></svg>About</a>
    <a class="nav-item"><svg viewBox="0 0 16 16"><path d="M6 12V3l7-1.5v9"/><circle cx="4.5" cy="12" r="1.7"/><circle cx="11.5" cy="10.5" r="1.7"/></svg>Listen</a>
    <a class="nav-item"><svg viewBox="0 0 16 16"><path d="M1 3h5.5c1 0 1.5.6 1.5 1.5V14c0-.8-.6-1.3-1.5-1.3H1zM15 3H9.5C8.5 3 8 3.6 8 4.5V14c0-.8.6-1.3 1.5-1.3H15z"/></svg>Read</a>
    <a class="nav-item"><svg viewBox="0 0 16 16"><circle cx="8" cy="8" r="7"/><path d="M6.5 5v6l4.5-3z"/></svg>Watch</a>
    <a class="nav-item"><svg viewBox="0 0 16 16"><rect x="2.5" y="1.5" width="11" height="13"/><path d="M5 5h6M5 8h6M5 11h6"/></svg>Forum</a>
    <a class="nav-item"><svg viewBox="0 0 16 16"><path d="M3 2h3l1.5 3.5-2 1.2a8 8 0 0 0 3.8 3.8l1.2-2L14 10v3c0 .6-.4 1-1 1A11 11 0 0 1 2 3c0-.6.4-1 1-1z"/></svg>Contact</a>
  </nav>
</header>

<section class="abs welcome">
  <h1>WELCOME TO BRIGHT YEARS NOOK</h1>
  <div class="rule"></div>
  <p>Lorem ipsum dolor sit amet, consectetuer adipiscing elit, sed diam nonummy nibh euismod tincidunt ut laoreet dolore magna aliquam erat volutpat. Ut wisi enim ad minim veniam, quis nostrud exerci tation ullamcorper suscipit lobortis nisl ut aliquip ex ea commodo consequat. Duis autem vel eum iriure dolor in hendrerit in vulputate velit esse molestie consequat, vel illum dolore eu feugiat nulla facilisis at vero eros et accumsan et iusto odio dignissim qui blandit praesent luptatum zzril delenit augue duis dolore te feugait nulla facilisi.</p>
</section>

<section class="abs features">
  <div class="abs feature" style="left:56px"><div class="thumb" role="img" aria-label="Photo of an older couple listening with earphones" style="background:linear-gradient(90deg,#cfcac2 0%,#8e8e8a 45%,#e3e1dc 55%,#9c9c98 100%)"></div><h2>Listen Podcasts</h2><p>Lorem ipsum dolor sit amet, consec<br>tetuer adipiscing elit</p><span class="more">[+]</span></div>
  <div class="abs feature" style="left:197px"><div class="thumb" role="img" aria-label="Photo of an older couple reading on a laptop" style="background:linear-gradient(90deg,#eef0ee 0%,#d9a8b0 45%,#c8b7ae 70%,#e6e6e4 100%)"></div><h2>Read Blog Post</h2><p>Lorem ipsum dolor sit amet, consec<br>tetuer adipiscing elit</p><span class="more">[+]</span></div>
  <div class="abs feature" style="left:338px"><div class="thumb" role="img" aria-label="Photo of an older couple watching a video on a phone" style="background:linear-gradient(90deg,#a9b3bf 0%,#cfc7b5 45%,#c9a77a 75%,#8d7a60 100%)"></div><h2>Watch Videos</h2><p>Lorem ipsum dolor sit amet, consec<br>tetuer adipiscing elit</p><span class="more">[+]</span></div>
  <div class="abs feature" style="left:479px"><div class="thumb" role="img" aria-label="Photo of a group of older friends outdoors" style="background:linear-gradient(180deg,#9fb56a 0%,#c9b89a 55%,#8aa3c9 100%)"></div><h2>Our Communities</h2><p>Lorem ipsum dolor sit amet, consec<br>tetuer adipiscing elit</p><span class="more">[+]</span></div>
</section>

<main class="abs content"></main>

<article class="abs post" style="top:700px">
  <div class="abs thumb" role="img" aria-label="Photo of older women playing dominoes" style="background:linear-gradient(90deg,#e0c56a 0%,#e6b040 40%,#7f9ac2 75%,#c8c2b4 100%)"></div>
  <h3 class="abs">Lorem ipsum dolor sit</h3>
  <div class="abs meta"><span><svg viewBox="0 0 8 8"><rect width="8" height="8" rx="1"/></svg>23/06/2016</span><span><svg viewBox="0 0 8 8"><ellipse cx="4" cy="3.5" rx="4" ry="3.2"/></svg>21 commets</span><span><svg viewBox="0 0 8 8"><path d="M0 3h2v5H0zM3 3l2-3c1 0 1 1 1 2h2v3l-1 3H3z"/></svg>Like Us</span><span><svg viewBox="0 0 8 8"><circle cx="6.5" cy="1.5" r="1.5"/><circle cx="1.5" cy="4" r="1.5"/><circle cx="6.5" cy="6.5" r="1.5"/><path d="M1.5 4 6.5 1.5M1.5 4l5 2.5" stroke="#8dc63f" stroke-width=".8"/></svg>Share</span></div>
  <p class="abs">Lorem ipsum dolor sit amet, consecit adipiscing elit, sed do eiusmod tempor incididunt labore n dolormae laboris ni ut aliquip ex ea lin consequat Duis aute lorem is irure dolor in reprehenderit magna aliqua. Ut enim ad is qnexercitation ullamco.</p>
  <div class="abs go"><svg width="9" height="9" viewBox="0 0 9 9"><path d="M1.5 1.5 4.5 4.5 1.5 7.5M4.5 1.5 7.5 4.5 4.5 7.5" fill="none" stroke="#fff" stroke-width="1"/></svg></div>
</article>

<article class="abs post" style="top:838px">
  <div class="abs thumb" role="img" aria-label="Photo of an older couple hiking in the mountains" style="background:linear-gradient(180deg,#7aa8d8 0%,#a8b8c8 30%,#5f7f48 60%,#7a5a3a 100%)"></div>
  <h3 class="abs">Lorem ipsum dolor sit</h3>
  <div class="abs meta"><span><svg viewBox="0 0 8 8"><rect width="8" height="8" rx="1"/></svg>19/03/2015</span><span><svg viewBox="0 0 8 8"><ellipse cx="4" cy="3.5" rx="4" ry="3.2"/></svg>21 commets</span><span><svg viewBox="0 0 8 8"><path d="M0 3h2v5H0zM3 3l2-3c1 0 1 1 1 2h2v3l-1 3H3z"/></svg>Like Us</span><span><svg viewBox="0 0 8 8"><circle cx="6.5" cy="1.5" r="1.5"/><circle cx="1.5" cy="4" r="1.5"/><circle cx="6.5" cy="6.5" r="1.5"/><path d="M1.5 4 6.5 1.5M1.5 4l5 2.5" stroke="#8dc63f" stroke-width=".8"/></svg>Share</span></div>
  <p class="abs">Lorem ipsum dolor sit amet, consecit adipiscing elit, sed do eiusmod tempor incididunt labore n dolormae laboris ni ut aliquip ex ea lin consequat Duis aute lorem is irure dolor in reprehenderit magna aliqua. Ut enim ad is qnexercitation ullamco.</p>
  <div class="abs go"><svg width="9" height="9" viewBox="0 0 9 9"><path d="M1.5 1.5 4.5 4.5 1.5 7.5M4.5 1.5 7.5 4.5 4.5 7.5" fill="none" stroke="#fff" stroke-width="1"/></svg></div>
</article>

<article class="abs post" style="top:977px">
  <div class="abs thumb" role="img" aria-label="Photo of a smiling family with a grandmother" style="background:linear-gradient(90deg,#d9a060 0%,#e8e3da 45%,#4f7fc0 80%,#3d6bb0 100%)"></div>
  <h3 class="abs">Lorem ipsum dolor sit</h3>
  <div class="abs meta"><span><svg viewBox="0 0 8 8"><rect width="8" height="8" rx="1"/></svg>23/06/2016</span><span><svg viewBox="0 0 8 8"><ellipse cx="4" cy="3.5" rx="4" ry="3.2"/></svg>21 commets</span><span><svg viewBox="0 0 8 8"><path d="M0 3h2v5H0zM3 3l2-3c1 0 1 1 1 2h2v3l-1 3H3z"/></svg>Like Us</span><span><svg viewBox="0 0 8 8"><circle cx="6.5" cy="1.5" r="1.5"/><circle cx="1.5" cy="4" r="1.5"/><circle cx="6.5" cy="6.5" r="1.5"/><path d="M1.5 4 6.5 1.5M1.5 4l5 2.5" stroke="#8dc63f" stroke-width=".8"/></svg>Share</span></div>
  <p class="abs">Lorem ipsum dolor sit amet, consecit adipiscing elit, sed do eiusmod tempor incididunt labore n dolormae laboris ni ut aliquip ex ea lin consequat Duis aute lorem is irure dolor in reprehenderit magna aliqua. Ut enim ad is qnexercitation ullamco.</p>
  <div class="abs go"><svg width="9" height="9" viewBox="0 0 9 9"><path d="M1.5 1.5 4.5 4.5 1.5 7.5M4.5 1.5 7.5 4.5 4.5 7.5" fill="none" stroke="#fff" stroke-width="1"/></svg></div>
</article>

<svg class="abs spinner" viewBox="0 0 24 24" aria-label="Loading more posts">
  <g stroke="#8dc63f" stroke-width="2" stroke-linecap="round">
    <path d="M12 2v4"/><path d="M12 18v4"/><path d="M2 12h4"/><path d="M18 12h4"/>
    <path d="M4.9 4.9l2.8 2.8"/><path d="M16.3 16.3l2.8 2.8"/><path d="M4.9 19.1l2.8-2.8"/><path d="M16.3 7.7l2.8-2.8"/>
  </g>
</svg>

<aside>
  <div class="abs promo promo-photo" role="img" aria-label="Advertisement photo of a person leaping on a beach">
    <div class="headline">There's No<br>Such Thing As<br>A Boring Photo<small>(Just Boring Photo Editors)</small></div>
    <div class="cta">Start Having Fun</div>
    <span class="badge" style="left:94px"></span><span class="badge" style="left:138px"></span>
  </div>
  <div class="abs promo promo-retire" role="img" aria-label="Advertisement photo of a retired man reading a newspaper outdoors">
    <div class="caption">Making Retirement A Pleasurable experience!</div>
  </div>
  <div class="abs promo promo-travel" role="img" aria-label="Travel advertisement with an aerial view of a tropical island">
    <div class="label">Mon été, je le vois<br>20% lézard, 80% poisson</div>
    <span class="tag"></span>
  </div>
  <div class="abs promo promo-books" role="img" aria-label="Illustration of an old library with stacks of books">
    <div class="line">YOU ARE WHAT YOU READ.</div>
  </div>
</aside>

<footer class="abs site-footer">Copyright © 2016 · BRIGHT YEARS NOOK · Terms and Conditions · Privacy Policy · Affiliate Disclaimer · Not affiliated with Founder Digest</footer>

</body>
</html>
```